We need a business card design for a new company located in Brampton Ontario Canada. Our goal is to promote companies to use our service as an "External Program Management " firm taking their industrial product concepts " from prototype to production." We would like to use blue and yellow as our colors. Our skills include finding suppliers for prototype parts and developing them into supplying not only prototypes but the final production parts as well for our customer base.
Colin Treadway
Sales Manager
VORMEL Solutions Inc.
14 Hollowmere Lane
Brampton, Ontario L3P 8K2
Canada
Phone: 905-417-2956
Fax: 905-417-2956
website: www.vormelsolutions.example
Email: colin@vormelsolutions.example

```html
<!DOCTYPE html>
<html lang="en">
<head>
<meta charset="utf-8">
<title>VORMEL Solutions Inc. – Business Card</title>
<link rel="stylesheet" href="https://fonts.googleapis.com/css2?family=Open+Sans:wght@400;600;700&display=swap">
<style>
  :root {
    --backdrop: #e9ebee;
    --card-white: #ffffff;
    --blue-light: #2f9fdc;
    --blue-deep: #0b5ea8;
    --accent-yellow: #f4e81c;
    --brand-navy: #1d3c8c;
    --text-dark: #333840;
    --icon-blue: #1d5fa5;
  }
  html, body {
    margin: 0;
    padding: 0;
    width: 1200px;
    height: 913px;
    overflow: hidden;
    background: var(--backdrop);
    font-family: "Open Sans", Arial, sans-serif;
  }
  .business-card {
    position: absolute;
    left: 150px;
    top: 200px;
    width: 900px;
    height: 514px;
    background: var(--card-white);
    overflow: hidden;
    box-shadow: 0 10px 30px rgba(0,0,0,0.18);
  }
  .card-swoosh {
    position: absolute;
    inset: 0;
    width: 900px;
    height: 514px;
  }
  .brand-mark {
    position: absolute;
    left: 70px;
    top: 160px;
    display: flex;
    align-items: center;
    gap: 14px;
  }
  .brand-square {
    width: 26px;
    height: 26px;
    background: var(--accent-yellow);
  }
  .brand-name {
    font-size: 32px;
    font-weight: 700;
    color: var(--brand-navy);
    letter-spacing: 0.5px;
  }
  .person {
    position: absolute;
    left: 440px;
    top: 228px;
    width: 220px;
    text-align: right;
  }
  .person-name {
    font-size: 21px;
    color: var(--text-dark);
    margin: 0;
    font-weight: 400;
    white-space: nowrap;
  }
  .person-title {
    font-size: 14px;
    color: var(--text-dark);
    margin: 2px 0 0;
  }
  .contact-list {
    position: absolute;
    left: 70px;
    top: 330px;
    margin: 0;
    padding: 0;
    list-style: none;
  }
  .contact-list li {
    display: flex;
    align-items: center;
    gap: 14px;
    font-size: 19px;
    color: var(--text-dark);
    height: 30px;
  }
  .contact-list li.strong { font-weight: 600; }
  .contact-icon { width: 18px; height: 18px; flex: none; }
</style>
</head>
<body>
  <article class="business-card">
    <svg class="card-swoosh" viewBox="0 0 900 514" aria-hidden="true">
      <defs>
        <linearGradient id="swooshBlue" x1="0" y1="0" x2="0.6" y2="1">
          <stop offset="0" stop-color="var(--blue-light)"/>
          <stop offset="1" stop-color="var(--blue-deep)"/>
        </linearGradient>
      </defs>
      <path d="M235,0 L900,0 L900,514 L776,514 C756,210 610,22 235,0 Z" fill="var(--accent-yellow)"/>
      <path d="M262,0 L900,0 L900,514 L790,514 C772,200 630,10 262,0 Z" fill="url(#swooshBlue)"/>
    </svg>

    <div class="brand-mark">
      <span class="brand-square"></span>
      <span class="brand-name">VORMEL Solutions Inc.</span>
    </div>

    <div class="person">
      <p class="person-name">Name Surname</p>
      <p class="person-title">Designation</p>
    </div>

    <ul class="contact-list">
      <li>
        <svg class="contact-icon" viewBox="0 0 18 18"><rect x="5" y="2" width="8" height="14" rx="1.5" fill="none" stroke="var(--icon-blue)" stroke-width="1.8"/></svg>
        0000 000 000
      </li>
      <li>
        <svg class="contact-icon" viewBox="0 0 18 18"><path d="M2,7 Q9,1 16,7 L14,9 L12,7 L6,7 L4,9 Z" fill="var(--icon-blue)"/><rect x="4" y="9" width="10" height="6" rx="1" fill="var(--icon-blue)"/></svg>
        0000 000 000
      </li>
      <li class="strong">
        <svg class="contact-icon" viewBox="0 0 18 18"><rect x="2" y="4" width="14" height="10" fill="none" stroke="var(--icon-blue)" stroke-width="1.6"/><path d="M2,4 L9,10 L16,4" fill="none" stroke="var(--icon-blue)" stroke-width="1.6"/></svg>
        name@webaddress.com
      </li>
      <li class="strong">
        <svg class="contact-icon" viewBox="0 0 18 18"><circle cx="9" cy="9" r="7" fill="none" stroke="var(--icon-blue)" stroke-width="1.6"/><ellipse cx="9" cy="9" rx="3" ry="7" fill="none" stroke="var(--icon-blue)" stroke-width="1.2"/><line x1="2" y1="9" x2="16" y2="9" stroke="var(--icon-blue)" stroke-width="1.2"/></svg>
        www.webaddress.com
      </li>
    </ul>
  </article>
</body>
</html>
```